New Business Card Design Project

Hi,

I'd like to create a logo for my business www.tellwickandtide.com. You will need to download two fonts for the business card: Lobster & Noticia Text. The fonts are free to download. No logo required.

Potential design idea:
One side hot pink (white font), one side white (grey font)
- On one side, hot pink similar to the pink on the website.
- Show Tellwick + Tide plus "your always-open wardrobe" in white font
- We really need it to be sleek, minimalistic and bright
- On the other side, we need to show our instagram and facebook URLs (fb.com/tellwickandtide, instagram.com/tellwickandtide). Please use the same dark grey font as our website and use a hollowed out grey FB & Instagram logo
We also need to show the following details, website, space for name and email (hello@tellwickandtide.com).

Feel free to go as creative as you would like! The above is a safe template that we know will satisfy our needs. Aim is to minimalist, simple and bold. , Details for my new Business Card Design Project will be added soon.

• Needs to fit the prell.com luxe business card template.

```html
<!DOCTYPE html>
<html lang="en">
<head>
<meta charset="utf-8">
<title>Tellwick + Tide — business card</title>
<link rel="stylesheet" href="https://fonts.googleapis.com/css2?family=Noticia+Text:wght@400;700&display=swap">
<style>
  :root {
    --backdrop: #1b1b1b;
    --card-white: #ffffff;
    --hot-pink: #e2177c;
    --ink-grey: #3c3c3c;
    --white: #ffffff;
  }
  * { box-sizing: border-box; margin: 0; padding: 0; }
  html, body { width: 1200px; height: 800px; overflow: hidden; }
  body {
    background: var(--backdrop);
    font-family: "Noticia Text", Georgia, serif;
    position: relative;
  }
  .card {
    position: absolute;
    top: 230px;
    width: 520px;
    height: 340px;
    box-shadow: 0 10px 30px rgba(0,0,0,.5);
  }
  .card--front { left: 50px; background: var(--card-white); color: var(--ink-grey); }
  .card--back { left: 630px; background: var(--hot-pink); color: var(--white); }

  .business-name {
    position: absolute; left: 0; right: 0; text-align: center;
    font-weight: 700; font-size: 34px; line-height: 1; white-space: nowrap;
  }
  .card--front .business-name { top: 46px; color: var(--ink-grey); }
  .card--back .business-name { top: 96px; color: var(--white); }

  .brace {
    position: absolute; top: 112px; font-size: 150px; line-height: 1;
    font-weight: 400; color: var(--ink-grey);
  }
  .brace--open { left: 78px; }
  .brace--close { right: 78px; }

  .contact {
    position: absolute; top: 116px; left: 0; right: 0; text-align: center;
    font-size: 19px; line-height: 27px;
  }
  .contact-name { font-weight: 700; font-size: 22px; margin-bottom: 4px; }
  .social {
    margin-top: 12px; display: flex; justify-content: center; align-items: center; gap: 8px;
    font-size: 17px;
  }
  .social-mark { width: 18px; height: 18px; border: 2px solid var(--ink-grey); border-radius: 3px; }

  .divider {
    position: absolute; top: 156px; left: 110px; right: 110px; height: 1.5px;
    background: var(--white);
  }
  .tagline {
    position: absolute; top: 182px; left: 0; right: 0; text-align: center;
    font-size: 24px; font-weight: 400; color: var(--white);
  }
</style>
</head>
<body>
  <section class="card card--front" aria-label="Card front">
    <p class="business-name">Tellwick + Tide</p>
    <div class="brace brace--open">{</div>
    <div class="brace brace--close">}</div>
    <div class="contact">
      <p class="contact-name">Mara Quill</p>
      <p class="contact-web">www.tellwickandtide.com</p>
      <p class="contact-email">hello@tellwickandtide.com</p>
      <p class="social"><span class="social-mark"></span><span class="social-handle">tellwickandtide</span></p>
    </div>
  </section>

  <section class="card card--back" aria-label="Card back">
    <p class="business-name">Tellwick + Tide</p>
    <div class="divider"></div>
    <p class="tagline">your always-open wardrobe</p>
  </section>
</body>
</html>
```